Business Card Design Project For Moving Company

Hello,

We need the business card to be 2 sided and we were thinking to use the logo on the front of the card (see file 1 attached) and the text "logo" (see file 2 attached) in the back of the card. We're looking for a powerful design that will help us build our brand, as our company is new.
We are a full service moving company (no storage) located in San Diego, CA, USA. The design should communicate to our potential customers that we have the highest level of service, customer satisfaction is our number one goal, our team is professional and efficient.

Thank you,

Dorn
Updates

Project Deadline Extended
Reason: We would like to have more time to provide feedback for the designs already submitted. Thank you, Dorn

Industry/Entity Type

Moving Company

Requirements
Must have
• Front of the card must have the following text and logo:
Haulbright, Inc
Residential And Commercial
Local And Long Distance
Address: 7312 Quillmont Rd, #146,
San Diego, CA, 92784
P: 855-372-LIFT (5438)
F: 858-529-4407
info@haul-bright.com
www.haul-bright.com

Back of the card must have the following text and text "logo" (file 2 attached):

The best compliment we can ever receive is a referral from our clients.

```html
<!DOCTYPE html>
<html lang="en">
<head>
<meta charset="utf-8">
<title>Haulbright, Inc — Business Card</title>
<link rel="stylesheet" href="https://fonts.googleapis.com/css2?family=Arimo:wght@400;700&display=swap">
<style>
  :root {
    --navy: #1b2447;
    --red: #d9261f;
    --white: #ffffff;
    --backdrop: #e9eaec;
    --card-w: 720px;
    --card-h: 411px;
  }
  * { box-sizing: border-box; margin: 0; padding: 0; }
  html, body {
    width: 1200px;
    height: 893px;
    overflow: hidden;
  }
  body {
    background: var(--backdrop);
    font-family: "Arimo", Arial, sans-serif;
    display: flex;
    flex-direction: column;
    align-items: center;
    justify-content: center;
    gap: 24px;
  }
  .card {
    position: relative;
    width: var(--card-w);
    height: var(--card-h);
    background: var(--navy);
    overflow: hidden;
    color: var(--white);
  }
  .card__stripe {
    position: absolute;
    left: 0;
    right: 0;
    bottom: 0;
    height: 18px;
    background: var(--red);
  }
  .card__art {
    position: absolute;
    background: var(--red);
  }
  .wordmark {
    font-family: "Arimo", Arial, sans-serif;
    font-weight: 700;
    color: var(--white);
    letter-spacing: 0.5px;
    line-height: 1;
    white-space: nowrap;
  }

  /* Front */
  .card--front .card__art {
    left: 528px;
    width: 150px;
    top: 0;
    bottom: 18px;
  }
  .front__text {
    position: absolute;
    left: 60px;
    top: 36px;
    width: 400px;
    text-align: center;
  }
  .front__text .wordmark {
    font-size: 46px;
  }
  .services {
    margin-top: 12px;
    font-weight: 700;
    font-size: 21px;
    line-height: 1.2;
  }
  .services .dot {
    display: inline-block;
    width: 6px;
    height: 6px;
    margin: 0 6px 4px;
    background: var(--white);
    transform: rotate(45deg);
  }
  .contact {
    margin-top: 44px;
    font-style: normal;
    font-weight: 700;
    font-size: 15px;
    line-height: 1.3;
  }
  .contact__label { display: block; }
  .web {
    margin-top: 40px;
    font-weight: 700;
    font-size: 15px;
    line-height: 1.3;
  }

  /* Back */
  .card--back .card__art {
    left: 0;
    width: 150px;
    top: 0;
    bottom: 18px;
  }
  .back__mark {
    position: absolute;
    left: 190px;
    right: 30px;
    top: 150px;
    text-align: center;
  }
  .back__mark .wordmark { font-size: 54px; }
  .back__quote {
    margin-top: 26px;
    font-weight: 400;
    font-size: 17px;
    line-height: 1.4;
    color: var(--white);
  }
</style>
</head>
<body>

  <section class="card card--front" aria-label="Card front">
    <div class="front__text">
      <div class="wordmark">HAULBRIGHT</div>
      <p class="services">Residential<span class="dot"></span>Commercial<br>Local<span class="dot"></span>Long Distance</p>
      <address class="contact">
        <span class="contact__label">Address:</span>
        7312 Quillmont Rd, #146, San Diego, CA, 92784<br>
        P: 855-372-LIFT (5438)<br>
        F: 858-529-4407
      </address>
      <p class="web">info@haul-bright.com<br>www.haul-bright.com</p>
    </div>
    <div class="card__art" role="img" aria-label="Large red brand emblem decoration"></div>
    <div class="card__stripe"></div>
  </section>

  <section class="card card--back" aria-label="Card back">
    <div class="card__art" role="img" aria-label="Large red brand emblem decoration"></div>
    <div class="back__mark">
      <div class="wordmark">HAULBRIGHT</div>
      <p class="back__quote">The best compliment we can ever receive<br>is a referral from our clients.</p>
    </div>
    <div class="card__stripe"></div>
  </section>

</body>
</html>
```